Design an Invitation for a cool Black and White Party, printable

Hi everyone,

we are making a black and white party and need some invitations. Theme should be the silhouettes of us two (abstract) and then whatever you find cool.

There is some Text too, 4-6 sentences.

Obv. it has to be blaack&white :)

This has to be printable in postcard format.

EDIT: Added pivtures for the silhouettes.. For me it´s a duit, for the lady it´s a dress.. We are going for something like this, but cooler: [url removed, login to view]

EDIT: The text

--Start Text---
Ihr seid eingeladen zum Black & White Grillen!

Am 22. Juli dieses Jahres werfen wir ab 14 Uhr den Grill an und feiern zusammen bis spät in die Nacht. Über euer Erscheinen mit maximal 4 Begleitpersonen freuen wir uns. Für Grillfleisch und Getränke ist gesorgt…

So geht es: Zusagen - wann und mit wem ihr kommt. Herausputzen – in schwarz und weiß. Salate und Getränke eurer Wahl mitbringen – und ab in den Lindmoosgasse 3!

Es wird einen Fahrer geben, der von ca. 18 Uhr bis 4 Uhr alle nach Hause fährt, die getrunken haben. Schlafplätze sind limitiert – first come, first serve.

----End text----

```html
<!DOCTYPE html>
<html lang="de">
<head>
<meta charset="utf-8">
<title>Black &amp; White Grillen – Einladung</title>
<link rel="stylesheet" href="https://fonts.googleapis.com/css2?family=Marcellus&family=Alegreya:wght@400&display=swap">
<style>
  :root {
    --ink: #231f20;
    --paper: #ffffff;
    --pattern-dark: #1c1819;
    --pattern-mid: #3a3637;
    --pattern-light: #d6d4d5;
    --figure: #e4e4e4;
  }
  html, body {
    margin: 0;
    padding: 0;
    overflow: hidden;
    background: var(--paper);
  }
  .invitation {
    position: relative;
    width: 1000px;
    height: 1200px;
    overflow: hidden;
    background: var(--paper);
    font-family: "Alegreya", Georgia, serif;
  }
  .pattern-band {
    position: absolute;
    left: 0;
    width: 1000px;
    background: linear-gradient(180deg, var(--pattern-light) 0%, var(--pattern-mid) 35%, var(--pattern-dark) 65%, var(--pattern-mid) 100%);
  }
  .pattern-band--top { top: 0; height: 263px; }
  .pattern-band--bottom {
    top: 942px;
    height: 258px;
    background: linear-gradient(180deg, var(--pattern-mid) 0%, var(--pattern-dark) 40%, var(--pattern-mid) 75%, var(--pattern-light) 100%);
  }
  .main-panel {
    position: absolute;
    left: 0;
    top: 263px;
    width: 1000px;
    height: 679px;
    background: var(--ink);
    color: var(--paper);
  }
  .headline {
    position: absolute;
    left: 0;
    top: 40px;
    width: 972px;
    margin: 0;
    text-align: center;
    font-family: "Marcellus", Georgia, serif;
    font-weight: 400;
    font-size: 64px;
    line-height: 86px;
    letter-spacing: 0.5px;
    white-space: nowrap;
  }
  .intro, .note {
    position: absolute;
    left: 34px;
    width: 710px;
    margin: 0;
    font-size: 20.5px;
    line-height: 30px;
    white-space: nowrap;
  }
  .intro { top: 236px; }
  .note { top: 542px; }
  .instructions {
    position: absolute;
    left: 20px;
    top: 354px;
    width: 727px;
    height: 157px;
    box-sizing: border-box;
    padding: 12px 14px;
    background: var(--paper);
    color: var(--ink);
  }
  .instructions p {
    margin: 0;
    font-size: 20.5px;
    line-height: 28px;
    white-space: nowrap;
  }
  .couple-silhouette {
    position: absolute;
    left: 756px;
    top: 206px;
    width: 206px;
    height: 298px;
  }
</style>
</head>
<body>
  <div class="invitation">
    <div class="pattern-band pattern-band--top" role="img" aria-label="Dichtes schwarz-weißes Muster aus Kreisen und Ranken"></div>

    <section class="main-panel">
      <h1 class="headline">Ihr seid eingeladen zum<br>Black &amp; White Grillen!</h1>

      <p class="intro">Am 22. Juli dieses Jahres werfen wir ab 14 Uhr den Grill an und feiern<br>zusammen bis spät in die Nacht. Über euer Erscheinen mit maximal 4<br>Begleitpersonen freuen&nbsp; wir uns. Für Grillfleisch und Getränke ist gesorgt…</p>

      <div class="instructions">
        <p>So geht es: Zusagen -&nbsp; wann und mit wem ihr kommt. Herausputzen –<br>in schwarz und weiß. Salate und Getränke eurer Wahl mitbringen –<br>und ab in den<br>Lindmoosgasse 3!</p>
      </div>

      <p class="note">Es wird einen Fahrer geben, der von ca. 18 Uhr bis 4 Uhr alle nach<br>Hause fährt, die getrunken haben. Schlafplätze sind limitiert – first<br>come, first serve.</p>

      <svg class="couple-silhouette" viewBox="0 0 206 298" role="img" aria-label="Weiße Silhouette eines Paares: Frau im Kleid und Mann im Anzug">
        <rect x="0" y="0" width="206" height="298" rx="40" fill="var(--figure)"/>
      </svg>
    </section>

    <div class="pattern-band pattern-band--bottom" role="img" aria-label="Dichtes schwarz-weißes Muster aus Kreisen und Ranken"></div>
  </div>
</body>
</html>
```